Counseling Design Website

My husband and I are both counselors and have a business called T & K counseling. We have already purchased a logo from you in October of 2022. We both have expertise in Autism, Dyslexia, ADHD, Couples Counseling, Marriage and Family counseling, and Geriatrics. I would also like to have my forms online. I am planning on using Google sites. I have started a site, but havent gotten very far. I would like to have it created where i can just copy and paste so to speak.
https://pages.brivexa.net/d/47kPzq2Hx8D-LN_cT5uQwE83BVKLpYmda/p/2ZRTe8uPwJ6bxnsr5WLVLOuVVSSQxFBRT/edit

```html
<!DOCTYPE html>
<html lang="en">
<head>
<meta charset="utf-8">
<title>T&amp;K Counselling</title>
<link href="https://fonts.googleapis.com/css2?family=Montserrat:wght@400;500;600&family=Lato:wght@400;700&display=swap" rel="stylesheet">
<style>
:root{
  --purple:#7b4ff0;
  --ink:#2b2b2b;
  --text:#444;
  --white:#fff;
  --footer:#222;
  --footer-line:#444;
  --footer-text:#e9e9e9;
  --hero-light:#e6e5ea;
}
*{box-sizing:border-box;margin:0;padding:0}
html,body{width:725px;height:1200px;overflow:hidden;background:var(--white)}
body{font-family:"Montserrat",sans-serif;color:var(--ink);position:relative}

.site-header{position:absolute;top:0;left:0;width:725px;height:44px;background:var(--white);z-index:2}
.brand{position:absolute;left:67px;top:0;width:75px;height:93px;background:var(--white);
  clip-path:polygon(0 0,100% 0,100% 64%,0 100%);
  display:flex;flex-direction:column;align-items:center;padding-top:14px;gap:6px}
.brand-name{font-size:8px;font-weight:500;color:var(--purple);white-space:nowrap}
.brand-dot{width:14px;height:14px;border-radius:50%;background:var(--purple)}
.main-nav{position:absolute;right:67px;top:10px;display:flex;align-items:center;gap:17px;font-size:9.5px}
.main-nav a{color:var(--ink);text-decoration:none}
.main-nav a.active{color:var(--purple);font-weight:500}
.btn{display:inline-flex;align-items:center;justify-content:center;background:var(--purple);color:var(--white);text-decoration:none}
.main-nav .btn{width:73px;height:25px;color:var(--white);margin-left:1px}

.hero{position:absolute;top:44px;left:0;width:725px;height:310px;background:var(--hero-light)}
.hero-photo{position:absolute;left:0;top:0;width:460px;height:310px;
  background:
    radial-gradient(ellipse 90px 110px at 175px 95px,#8a6a5a 0%,rgba(138,106,90,.55) 45%,rgba(138,106,90,0) 100%),
    radial-gradient(ellipse 150px 130px at 110px 240px,#7d7874 0%,rgba(125,120,116,.6) 50%,rgba(125,120,116,0) 100%),
    radial-gradient(ellipse 120px 60px at 320px 270px,#f4f4f6 0%,rgba(244,244,246,0) 100%),
    linear-gradient(90deg,#b4b0ae 0%,#cdcacb 40%,#dfdee2 75%,var(--hero-light) 100%)}
.hero-copy{position:absolute;left:440px;top:50px;width:220px}
.hero-kicker{font-size:18.5px;font-weight:500;color:var(--purple)}
.hero-title{font-size:26.5px;font-weight:600;color:var(--purple);margin-top:4px;white-space:nowrap}
.hero-text{font-size:9.3px;line-height:17px;color:var(--text);margin-top:12px}
.hero .btn{width:73px;height:25px;font-size:9.5px;margin-top:16px}

.services{position:absolute;top:395px;left:67px;width:591px}
.section-title{text-align:center;font-size:26px;font-weight:600;color:var(--purple)}
.service-grid{display:grid;grid-template-columns:repeat(3,189px);column-gap:12px;row-gap:25px;margin-top:25px}
.service-card{height:229px;background:var(--white);box-shadow:0 2px 8px rgba(0,0,0,.06);text-align:center;position:relative}
.service-photo{height:131px}
.service-icon{position:absolute;left:70px;top:95px;width:49px;height:49px;background:var(--white);
  box-shadow:0 2px 6px rgba(0,0,0,.1);display:flex;align-items:center;justify-content:center}
.service-icon svg{width:28px;height:28px;fill:none;stroke:var(--purple);stroke-width:1.4;stroke-linecap:round;stroke-linejoin:round}
.service-name{font-size:11px;font-weight:500;margin-top:32px}
.service-text{font-size:9px;line-height:14.5px;color:var(--text);margin-top:6px}

.site-footer{position:absolute;top:983px;left:0;width:725px;height:217px;background:var(--footer);color:var(--footer-text);font-family:"Lato",sans-serif}
.footer-cols{position:absolute;left:67px;top:37px;width:591px;height:110px}
.footer-col{position:absolute;top:0}
.footer-col h3{font-family:"Montserrat",sans-serif;font-size:9.5px;font-weight:500;color:var(--white)}
.footer-col ul{list-style:none;margin-top:19px;font-size:8px;line-height:15.5px}
.col-contact{left:1px}
.col-services{left:227px}
.col-links{left:514px}
.divider{position:absolute;top:3px;width:1px;height:110px;background:var(--footer-line)}
.services-list{display:grid;grid-template-columns:111px auto}
.contact-list li{display:flex;gap:8px;margin-bottom:6px}
.contact-list svg{width:8px;height:9px;flex:none;margin-top:3px;fill:var(--purple)}
.footer-bottom{position:absolute;left:67px;top:177px;width:591px;border-top:1px solid var(--footer-line);
  text-align:center;font-family:"Montserrat",sans-serif;font-size:8.5px;padding-top:16px}
</style>
</head>
<body>

<header class="site-header">
  <div class="brand">
    <span class="brand-name">T &amp; K counseling</span>
    <span class="brand-dot"></span>
  </div>
  <nav class="main-nav">
    <a class="active" href="#">Home</a>
    <a href="#">About</a>
    <a href="#">Services</a>
    <a href="#">Blog</a>
    <a href="#">Contact</a>
    <a class="btn" href="#">Get a quote</a>
  </nav>
</header>

<section class="hero">
  <div class="hero-photo" role="img" aria-label="Photo of a smiling woman in a grey cardigan working on a laptop in a bright room"></div>
  <div class="hero-copy">
    <p class="hero-kicker">Welcome to</p>
    <h1 class="hero-title">T&amp;K Counselling</h1>
    <p class="hero-text">Lorem ipsum dolor sit amet, conse adipi scing elit, sed do eiusmod tempor incididt ut labore et dolore magna qua. Quis ipsum suspendisse ultrices gravida. Risus commoverra maecenas accumsan lacus vel facilisis.</p>
    <a class="btn" href="#">Learn More</a>
  </div>
</section>

<main class="services">
  <h2 class="section-title">Our Services</h2>
  <div class="service-grid">
    <article class="service-card">
      <div class="service-photo" role="img" aria-label="Photo of a laughing young boy playing with a hand puppet" style="background:linear-gradient(135deg,#e9e2dc,#b9473a 60%,#7d4a33)"></div>
      <div class="service-icon"><svg viewBox="0 0 28 28"><path d="M6 6h7v3a2 2 0 1 0 4 0V6h5v7h-3a2 2 0 1 0 0 4h3v5H6z"/></svg></div>
      <h3 class="service-name">Autism</h3>
      <p class="service-text">Ut enim ad minima veniam,<br>nostrum exercitationem ullam</p>
    </article>
    <article class="service-card">
      <div class="service-photo" role="img" aria-label="Photo of a schoolboy thinking over his homework at a desk" style="background:linear-gradient(135deg,#eceae6,#c9b49a 55%,#6f7380)"></div>
      <div class="service-icon"><svg viewBox="0 0 28 28"><path d="M5 8a3 3 0 1 1 4 3v2M9 16v.5M17 7a3 3 0 1 1 4 3v2M21 15v.5M12 22h5"/></svg></div>
      <h3 class="service-name">Dyslexia</h3>
      <p class="service-text">Ut enim ad minima veniam,<br>nostrum exercitationem ullam</p>
    </article>
    <article class="service-card">
      <div class="service-photo" role="img" aria-label="Photo of a daydreaming boy resting his head in a classroom" style="background:linear-gradient(135deg,#d9cfb4,#c9c4bb 50%,#8fa8c9)"></div>
      <div class="service-icon"><svg viewBox="0 0 28 28"><path d="M14 14a1.5 1.5 0 1 1 1.5-1.5A4 4 0 1 1 10 15a6.5 6.5 0 1 1 11-4"/></svg></div>
      <h3 class="service-name">ADHD</h3>
      <p class="service-text">Ut enim ad minima veniam,<br>nostrum exercitationem ullam</p>
    </article>
    <article class="service-card">
      <div class="service-photo" role="img" aria-label="Photo of a couple in a counselling session" style="background:linear-gradient(135deg,#d8d4cf,#a89c8c 55%,#6b6e7a)"></div>
      <div class="service-icon"><svg viewBox="0 0 28 28"><circle cx="9" cy="13" r="2.5"/><circle cx="19" cy="13" r="2.5"/><path d="M4 23v-3a5 5 0 0 1 10 0v3M14 23v-3a5 5 0 0 1 10 0v3M5 4h7v4H5zM16 4h7v4h-7z"/></svg></div>
      <h3 class="service-name">Couples Counseling</h3>
      <p class="service-text">Ut enim ad minima veniam,<br>nostrum exercitationem ullam</p>
    </article>
    <article class="service-card">
      <div class="service-photo" role="img" aria-label="Photo of a family talking with a counsellor in a living room" style="background:linear-gradient(135deg,#ece8e2,#c8a27a 55%,#a0442e)"></div>
      <div class="service-icon"><svg viewBox="0 0 28 28"><circle cx="11" cy="16" r="6"/><circle cx="18" cy="15" r="6"/><path d="M9 8l2-3 2 3"/></svg></div>
      <h3 class="service-name">Marriage &amp; Family counselling</h3>
      <p class="service-text">Ut enim ad minima veniam,<br>nostrum exercitationem ullam</p>
    </article>
    <article class="service-card">
      <div class="service-photo" role="img" aria-label="Photo of a carer helping an elderly man with a puzzle game" style="background:linear-gradient(135deg,#dfe3df,#5b86c2 45%,#c7b79c)"></div>
      <div class="service-icon"><svg viewBox="0 0 28 28"><circle cx="13" cy="5" r="2"/><path d="M12 9l-2 6 3 2-1 7M14 10l3 4M18 14v10M10 15l-2 9"/></svg></div>
      <h3 class="service-name">Geriatrics</h3>
      <p class="service-text">Ut enim ad minima veniam,<br>nostrum exercitationem ullam</p>
    </article>
  </div>
</main>

<footer class="site-footer">
  <div class="footer-cols">
    <div class="footer-col col-contact">
      <h3>CONTACT INFO</h3>
      <ul class="contact-list">
        <li><svg viewBox="0 0 8 10"><path d="M4 0a3.5 3.5 0 0 1 3.5 3.5C7.5 6 4 10 4 10S.5 6 .5 3.5A3.5 3.5 0 0 1 4 0zm0 2a1.5 1.5 0 1 0 0 3 1.5 1.5 0 0 0 0-3z"/></svg><span>T&amp;K Counselling,<br>Address comes here</span></li>
        <li><svg viewBox="0 0 8 10"><path d="M1 0h6v10H1zm1 1v7h4V1z"/></svg><span>Ph: _1800-555-0142</span></li>
        <li><svg viewBox="0 0 8 10"><path d="M0 2h8v6H0zm0 0l4 3 4-3"/></svg><span>info@tkcounselling.example</span></li>
      </ul>
    </div>
    <span class="divider" style="left:188px"></span>
    <div class="footer-col col-services">
      <h3>SERVICES</h3>
      <ul class="services-list">
        <li>Autism</li><li>Marriage and Family counselling</li>
        <li>Dyslexia</li><li>Geriatrics</li>
        <li>ADHD</li><li></li>
        <li>Couples Counseling</li><li></li>
      </ul>
    </div>
    <span class="divider" style="left:467px"></span>
    <div class="footer-col col-links">
      <h3>OTHER LINKS</h3>
      <ul>
        <li>Terms &amp; Conditions</li>
        <li>Privacy Policy</li>
        <li>Cookies</li>
        <li>Contact</li>
        <li>Blog</li>
      </ul>
    </div>
  </div>
  <div class="footer-bottom">2023 T&amp;K Counselling. All Rights Reserved.</div>
</footer>

</body>
</html>
```